Save the date: email notification

I need a "Save the Date" email notification design for my wedding:

Objetives:

1.- to notify friends about our future wedding ( by sending an email)
2.- to request our friends to send us their phisical address. ( reply to the email)

It will not be the formal invitation for the wedding, just an announcement.

Wedding Date: 15-sep-2012
Our names: Lucía & Rodrigo

Target Market(s)

friends, family and other commitments

Industry/Entity Type

Wedding

Requirements
Must have
• Wedding Date: 15-sep-2012
Our names: Lucía & Rodrigo

```html
<!DOCTYPE html>
<html lang="en">
<head>
<meta charset="utf-8">
<title>Save the Date – Lucía &amp; Rodrigo</title>
<link href="https://fonts.googleapis.com/css2?family=Caveat+Brush&amp;family=Arimo:ital,wght@0,700;1,700&amp;display=swap" rel="stylesheet">
<style>
  :root {
    --plum-ink: #4a0f3d;
    --card-glow: #921f7c;
    --card-mid: #6b1a5c;
    --card-deep: #3e0f33;
    --card-night: #150611;
    --text-light: #ffffff;
    --paper: #ffffff;
  }
  * { margin: 0; padding: 0; box-sizing: border-box; }
  html, body { width: 1200px; height: 857px; overflow: hidden; background: var(--paper); }
  body { position: relative; font-family: "Arimo", Arial, sans-serif; }

  .recipient {
    position: absolute; left: 152px; top: 30px;
    color: var(--plum-ink); font-style: italic; font-weight: 700;
    font-size: 20px; line-height: 27px;
  }
  .headline {
    position: absolute; left: 150px; top: 101px;
    color: var(--plum-ink); font-style: italic; font-weight: 700;
    font-size: 33px; letter-spacing: 0.5px;
  }

  .announcement-card {
    position: absolute; left: 143px; top: 145px;
    width: 925px; height: 661px; border-radius: 13px; overflow: hidden;
    background:
      linear-gradient(90deg, transparent 44%, rgba(10,2,8,0.55) 50%, transparent 56%),
      radial-gradient(ellipse 55% 45% at 50% 0%, var(--card-glow) 0%, rgba(146,31,124,0) 100%),
      linear-gradient(180deg, var(--card-mid) 0%, var(--card-deep) 55%, var(--card-night) 100%);
  }
  .announcement-card::after {
    content: ""; position: absolute; inset: 0;
    background: radial-gradient(ellipse 18% 45% at 50% 100%, rgba(5,2,4,0.8), transparent 100%);
  }

  .card-text { position: absolute; color: var(--text-light); font-weight: 700; z-index: 1; white-space: nowrap; }
  .lead { left: 0; width: 100%; text-align: center; top: 54px; font-size: 41px; transform: translateX(-9px); }
  .couple-names {
    left: 0; width: 100%; text-align: center; top: 125px;
    font-family: "Caveat Brush", cursive; font-weight: 400; font-size: 76px;
    transform: translateX(-8px);
  }
  .mirrored-line { left: 650px; top: 205px; font-size: 34px; }
  .married-line { left: 307px; top: 245px; font-size: 29px; }
  .wedding-date {
    left: 394px; top: 335px;
    font-family: "Caveat Brush", cursive; font-weight: 400; font-size: 88px;
  }
  .weekday { left: 550px; top: 480px; font-size: 34px; }

  .hearts-ornament { position: absolute; left: 28px; top: 285px; width: 296px; height: 343px; z-index: 1; }
</style>
</head>
<body>
  <p class="recipient">To,<br>Dear Friend....................................................</p>
  <h1 class="headline">Save the date : 15.09.2012</h1>

  <section class="announcement-card">
    <p class="card-text lead">Do remember</p>
    <p class="card-text couple-names">Lucía &amp; Rodrigo</p>
    <p class="card-text mirrored-line">era eW</p>
    <p class="card-text married-line">are getting married on</p>
    <p class="card-text wedding-date">15-sep-2012</p>
    <p class="card-text weekday">SATURDAY</p>

    <svg class="hearts-ornament" role="img" aria-label="Two intertwined ribbon hearts ornament" viewBox="0 0 296 343">
      <defs>
        <radialGradient id="heartGlow" cx="50%" cy="45%" r="55%">
          <stop offset="0%" stop-color="#8a2a78" stop-opacity="0.55"/>
          <stop offset="100%" stop-color="#3e0f33" stop-opacity="0"/>
        </radialGradient>
      </defs>
      <rect width="296" height="343" fill="url(#heartGlow)"/>
    </svg>
  </section>
</body>
</html>
```